Tidewell Gin - Label for new Gin bottle

I am looking for a bottle label for our small batch, handcrafted Gin. We are located in the bay-side city of Frankston (Victoria, Australia). I know I want more of a serious label but am torn between traditional or modern styling.

Label to include;
• Tidewell GIN (name)
• Hand Crafted
• Small Batch
• 40% Vol

Using 700ml MERIDA Spirit Bottle - Cork

Requirements
Must have
• Name; Tidewell Gin
Method: Hand Crafted
Batch Size; Small Batch
Alc; 40% Vol
Nice to have
• Maybe a coastal/seaside reference or reference to distilling.

```html
<!DOCTYPE html>
<html lang="en">
<head>
<meta charset="utf-8">
<title>Tidewell Gin – Bottle Label</title>
<link rel="stylesheet" href="https://fonts.googleapis.com/css2?family=Oswald:wght@300;400&display=swap">
<style>
  :root {
    --page-bg: #e8edf4;
    --pattern-tone: #d3d8df;
    --pattern-edge: #c4cad3;
    --navy-deep: #0c2238;
    --navy-mid: #1d3d5a;
    --navy-light: #5a84a6;
    --silver: #e4e8ee;
    --silver-dim: #c7ced8;
    --gold: #c9a83e;
    --rule: #b9c0ca;
  }
  * { margin: 0; padding: 0; box-sizing: border-box; }
  html, body {
    width: 960px;
    height: 1200px;
    overflow: hidden;
    background: var(--page-bg);
  }
  .label {
    position: absolute;
    left: 40px;
    top: 270px;
    width: 880px;
    height: 680px;
  }
  .label__pattern {
    position: absolute;
    left: 0;
    top: 0;
    width: 880px;
    height: 600px;
    background: linear-gradient(180deg, var(--pattern-tone), #dde1e7 50%, var(--pattern-tone));
    border-top: 2px solid var(--pattern-edge);
    border-bottom: 2px solid var(--pattern-edge);
  }
  .label__rule {
    position: absolute;
    left: 0;
    width: 880px;
    height: 1px;
    background: var(--rule);
  }
  .label__rule--top { top: 14px; }
  .label__rule--foot { top: 636px; }
  .label__rule--bottom { top: 586px; }
  .seal {
    position: absolute;
    left: 180px;
    top: 40px;
    width: 520px;
    height: 520px;
  }
  .seal__text {
    position: absolute;
    left: 0;
    width: 520px;
    text-align: center;
    font-family: "Oswald", sans-serif;
  }
  .seal__batch {
    top: 132px;
    font-size: 38px;
    font-weight: 300;
    color: var(--silver-dim);
    letter-spacing: 1px;
  }
  .seal__name {
    top: 190px;
    font-size: 112px;
    font-weight: 400;
    color: var(--silver);
    letter-spacing: 6px;
    line-height: 1;
  }
  .seal__divider {
    position: absolute;
    left: 160px;
    top: 342px;
    width: 200px;
    height: 2px;
    background: var(--gold);
  }
  .seal__gin {
    top: 354px;
    font-size: 58px;
    font-weight: 400;
    color: var(--gold);
    letter-spacing: 4px;
  }
  .footline {
    position: absolute;
    top: 614px;
    font-family: "Oswald", sans-serif;
    font-weight: 300;
  }
  .footline--method {
    left: 0;
    width: 880px;
    text-align: center;
    font-size: 36px;
    color: var(--gold);
    top: 606px;
  }
  .footline--abv { left: 18px; font-size: 28px; color: var(--silver-dim); }
  .footline--volume { right: 18px; font-size: 28px; color: var(--silver-dim); }
</style>
</head>
<body>
  <main class="label">
    <div class="label__pattern" role="img" aria-label="Silver interlaced geometric star pattern band"></div>
    <div class="label__rule label__rule--top"></div>
    <div class="label__rule label__rule--bottom"></div>

    <section class="seal">
      <svg width="520" height="520" viewBox="0 0 520 520" aria-hidden="true">
        <defs>
          <linearGradient id="sealShade" x1="0" y1="0" x2="1" y2="0">
            <stop offset="0" stop-color="var(--navy-deep)"/>
            <stop offset="0.3" stop-color="var(--navy-light)"/>
            <stop offset="0.55" stop-color="var(--navy-mid)"/>
            <stop offset="1" stop-color="var(--navy-deep)"/>
          </linearGradient>
        </defs>
        <circle cx="260" cy="260" r="258" fill="url(#sealShade)"/>
        <circle cx="260" cy="260" r="240" fill="none" stroke="var(--gold)" stroke-width="1.2"/>
        <circle cx="260" cy="260" r="234" fill="none" stroke="var(--gold)" stroke-width="0.8"/>
        <circle cx="260" cy="260" r="140" fill="none" stroke="var(--gold)" stroke-width="0.6" opacity="0.5"/>
      </svg>
      <p class="seal__text seal__batch">SMALL BATCH</p>
      <h1 class="seal__text seal__name">TIDEWELL</h1>
      <div class="seal__divider"></div>
      <p class="seal__text seal__gin">GIN</p>
    </section>

    <p class="footline footline--abv">40% Vol</p>
    <p class="footline footline--method">HAND CRAFTED</p>
    <p class="footline footline--volume">700ml</p>
  </main>
</body>
</html>
```